Window graphics needed for chiropractic office

I am looking to add perforated window vinyl graphic to my exterior office windows. I am looking for something professional and modern and clean and not too busy. I am open to using stock chiropractic photo/s but don't want anything with a spine diagram or person grabbing back in pain. I have included multiple files for you to review some of my ideas. I like the idea of covering all of the bottom windows with a pattern/design that matches my logo colors. (Hex #00pacd and #00ced1). Other complimentary colors are fine too. I have also included several other sample photos and noted what I liked about them. I have also included multiple versions of my logo. I usually use the one with the "Injury Care Clinic" in dark letters but have one in all white or white letters instead of dark if needed.

Target Market(s)

People recently injured in work and auto accidents and also people seeking wellness care for neck/back pain.

Industry/Entity Type

Healthcare/Chiropractic

Font styles to use
Serif
Sans Serif

Colors
0094D4
00A9DD
6FCCEA
C7EBF8
E9F6FB
00AB8E
00BBA5
67D7C9
C6EFE9
E9F9F6

Requirements
Must have
• See attached photo/diagram of which windows should/should not be covered. Black area must be entirely covered for patient privacy reason. Gray areas can be covered, uncovered or partially covered.
Nice to have
• I am open to having my logo on the windows but not too big since I already have a large LED sign on the opposite wall. Website and phone would be nice: www.spinewaveMKT.com and 555-281-7460. I am open to words listing some of the treats that we offered like "Laser Therapy", "Decompression" , "Chiropractic", "Manual Therapy", "Functional Rehabilitation" , "Auto Accidents", "Work Injuries", "Slip & Fall", "Wellness Care"
Should not have
• Any spine diagrams or person grasping back in pain.

```html
<!DOCTYPE html>
<html lang="en">
<head>
<meta charset="utf-8">
<title>SpineWave Window Graphics</title>
<link rel="stylesheet" href="https://fonts.googleapis.com/css2?family=Poppins:wght@500;700;800&display=swap">
<style>
  :root {
    --backdrop: #0f8c8b;
    --aqua: #00ced1;
    --sea: #2aa9c9;
    --sky: #5fb7e6;
    --white: #ffffff;
  }
  * { box-sizing: border-box; margin: 0; padding: 0; }
  html, body { width: 1200px; height: 1200px; overflow: hidden; }
  body {
    background: var(--backdrop);
    font-family: "Poppins", sans-serif;
    color: var(--white);
    position: relative;
  }
  .storefront { position: absolute; left: 0; width: 1200px; }
  .storefront-upper { top: 48px; height: 540px; }
  .storefront-lower { top: 680px; height: 390px; }
  .panel {
    position: absolute;
    background: var(--aqua);
    overflow: hidden;
  }
  .label {
    position: absolute;
    font-weight: 800;
    text-transform: uppercase;
    line-height: 0.98;
    letter-spacing: 0.5px;
    white-space: nowrap;
  }
  .photo-sea {
    background:
      linear-gradient(180deg, rgba(0,206,209,0) 55%, var(--aqua) 100%),
      linear-gradient(180deg, #6bbde9 0%, #3fa6d8 30%, #1f8fbf 48%, #2aa9c9 60%, #49c3cf 75%, var(--aqua) 100%);
  }
  .photo-couple {
    background:
      radial-gradient(ellipse 38% 45% at 35% 62%, rgba(240,240,235,0.75), rgba(240,240,235,0) 70%),
      radial-gradient(ellipse 34% 45% at 70% 64%, rgba(245,245,240,0.8), rgba(245,245,240,0) 70%),
      linear-gradient(180deg, #3f95dd 0%, #7fc3ea 30%, #2f8fc4 45%, #3ab3cf 70%, #8fd9dc 100%);
  }
  .photo-beach {
    background:
      radial-gradient(ellipse 16% 45% at 70% 50%, rgba(200,170,140,0.7), rgba(200,170,140,0) 75%),
      linear-gradient(180deg, rgba(0,206,209,0) 45%, var(--aqua) 100%),
      linear-gradient(180deg, #eef3f2 0%, #dfeceb 25%, #c9ddd6 38%, #dfe7e0 55%, #b9e2dc 75%, var(--aqua) 100%);
  }
  .photo-faded {
    background:
      radial-gradient(ellipse 45% 60% at 55% 50%, rgba(50,140,200,0.35), rgba(50,140,200,0) 70%),
      linear-gradient(135deg, #2bc6d6 0%, var(--aqua) 60%, #19d2d2 100%);
  }
  .brand {
    position: absolute;
    display: flex;
    align-items: center;
    gap: 6px;
  }
  .brand-mark { width: 18px; height: 18px; background: var(--white); flex: none; }
  .brand-name { font-weight: 700; font-size: 15px; line-height: 1; white-space: nowrap; }
  .brand-sub { font-weight: 500; font-size: 6px; letter-spacing: 0.3px; display: block; margin-top: 2px; }
  .mark-panel { display: flex; align-items: center; justify-content: center; }
  .mark-circle { width: 64px; height: 64px; border-radius: 50%; background: var(--white); }
  .vertical {
    position: absolute;
    transform: rotate(-90deg);
    transform-origin: left top;
    white-space: nowrap;
    font-weight: 800;
    text-transform: uppercase;
  }
  .pill {
    display: block;
    background: var(--white);
    color: var(--aqua);
    border-radius: 14px;
    font-weight: 800;
    text-align: center;
    margin: 0 auto;
  }
</style>
</head>
<body>

<section class="storefront storefront-upper">
  <div class="panel photo-sea" style="left:16px;top:146px;width:138px;height:273px" role="img" aria-label="Calm blue ocean horizon">
    <div class="brand" style="left:14px;top:14px">
      <span class="brand-mark"></span>
      <span class="brand-name">SpineWave<span class="brand-sub">INJURY CARE CLINIC</span></span>
    </div>
  </div>
  <div class="panel" style="left:16px;top:426px;width:136px;height:104px">
    <div class="label" style="left:18px;top:38px;font-size:15px">Auto<br>Accidents</div>
  </div>

  <div class="panel photo-couple" style="left:170px;top:154px;width:252px;height:267px" role="img" aria-label="Smiling couple crouching together on the beach"></div>
  <div class="panel" style="left:168px;top:430px;width:250px;height:102px">
    <div class="label" style="left:30px;top:30px;font-size:20px">Functional<br>Rehabilitation</div>
  </div>

  <div class="panel photo-faded" style="left:441px;top:0;width:126px;height:134px" role="img" aria-label="Faded photo of a chiropractic adjustment"></div>
  <div class="panel" style="left:438px;top:144px;width:124px;height:274px">
    <div class="vertical" style="left:24px;top:232px;font-size:36px;line-height:0.95">Work<br>Injuries</div>
  </div>
  <div class="panel mark-panel" style="left:436px;top:426px;width:122px;height:103px"><span class="mark-circle"></span></div>

  <div class="panel photo-beach" style="left:570px;top:142px;width:580px;height:274px" role="img" aria-label="Smiling woman drawing in the sand on a misty beach"></div>
  <div class="panel photo-faded" style="left:952px;top:-2px;width:200px;height:134px" role="img" aria-label="Faded photo of a relaxed patient receiving care"></div>

  <div class="panel photo-faded" style="left:568px;top:426px;width:254px;height:106px" role="img" aria-label="Faded photo of a person walking on a boardwalk">
    <div class="label" style="left:14px;top:36px;font-size:33px">Slip &amp; Fall</div>
  </div>
  <div class="panel mark-panel" style="left:830px;top:426px;width:110px;height:103px"><span class="mark-circle" style="width:58px;height:58px"></span></div>
  <div class="panel photo-faded" style="left:948px;top:424px;width:202px;height:106px" role="img" aria-label="Faded photo of a patient resting during treatment">
    <div class="label" style="left:40px;top:34px;font-size:26px">Wellness<br>Care</div>
  </div>
</section>

<section class="storefront storefront-lower">
  <div class="panel" style="left:32px;top:284px;width:106px;height:102px">
    <div class="label" style="left:4px;top:42px;font-size:10px">Decompression<br>Chiropractic</div>
  </div>
  <div class="panel photo-faded" style="left:154px;top:284px;width:244px;height:102px" role="img" aria-label="Faded photo of laser therapy treatment">
    <div class="label" style="left:112px;top:28px;font-size:23px">Laser<br>Therapy</div>
  </div>
  <div class="panel" style="left:406px;top:284px;width:106px;height:102px">
    <div class="label" style="left:10px;top:34px;font-size:15px">Manual<br>Therapy</div>
  </div>
  <div class="panel" style="left:524px;top:284px;width:254px;height:102px">
    <span class="pill" style="width:194px;height:26px;line-height:26px;font-size:11.5px;margin-top:22px">WWW.SPINEWAVEMKT.COM</span>
    <span class="pill" style="width:194px;height:26px;line-height:26px;font-size:16px;margin-top:13px">555-281-7460</span>
  </div>

  <div class="panel" style="left:962px;top:0;width:44px;height:272px">
    <div class="vertical" style="left:12px;top:258px;font-size:16px">www.spinewavemkt.com</div>
  </div>
  <div class="panel photo-sea" style="left:1014px;top:0;width:138px;height:272px" role="img" aria-label="Calm blue ocean horizon">
    <div class="brand" style="left:14px;top:14px">
      <span class="brand-mark"></span>
      <span class="brand-name">SpineWave<span class="brand-sub">INJURY CARE CLINIC</span></span>
    </div>
  </div>
  <div class="panel" style="left:962px;top:284px;width:44px;height:102px">
    <div class="vertical" style="left:12px;top:94px;font-size:17px">Visit Us</div>
  </div>
  <div class="panel" style="left:1014px;top:284px;width:138px;height:102px">
    <div class="label" style="left:20px;top:36px;font-size:15px">Auto<br>Accidents</div>
  </div>
</section>

</body>
</html>
```